Corvex PxTR PowerPoint Template

Template in Powerpoint 2010 format
The template is for Corvex Advisory Partners, a firm based in Calgary, Alberta, Canada. For more information on Corvex, see www.corvex-example.ca
The PowerPoint presentation will be used for yearly events called PATR (Tracing Every Pipeline) and PMTR (Tracing Many Pipelines). At these one-day conferences, Corvex shares expertise/knowledge in current oil and gas technology solutions. Topics covered include: Who are the vendors? What are their products? What are their relative strengths and weaknesses? and What trends do we see?
We intend to use the template for several years. As a result, we would like the title to be dynamic, that is, changed each year to reflect the passing of time as new events are held (for example, PMTR 2013, PMTR 2014).
Corvex conducts almost all of its business in downtown Calgary for white collar clients. Our clients are primarily upstream Oil and Gas companies. Event attendees are typically business facing IT resources or business people with IT solutions responsibilities. In otherwords, we are communicating to a corporate audience.
The presentations for PMTR and PATR are compiled by multiple teams and are then merged together. As a result, previous presentations have looked unprofessional with inconsistent graphics, logos, fonts, font sizes, colours, etc. Team members using the new PowerPoint template will require guidance (within the template) on how to use it properly to provide a common look.
An example of a powerpoint presentation for a previous PMTR event that was designed in-house is attached for your reference.
Desired master slides for new PowerPoint template:
- Overall Session - Title Slide
- Functional Area – Title slide
- Content slides, including title with content, comparison, picture with caption
- Predictions slide
- Thank you slide
Desired outcome:
- a fresh, professional looking design
- a consistent look and feel across the slide-deck
- a user-friendly template/master slides
Additional concepts that COULD be incorporated:
- upstream onshore oil and gas graphics
- technology or software
NOTE: GIF and JPG versions of the CAP logo are attached. The logo colours are Blue – Pantone 288, and Yellow – Pantone 129

```html
<!DOCTYPE html>
<html lang="en">
<head>
<meta charset="utf-8">
<title>Corvex PMTR Slide Template</title>
<link rel="stylesheet" href="https://fonts.googleapis.com/css2?family=Barlow:wght@400;500;600&display=swap">
<style>
:root{
  --blue:#233f7a;
  --yellow:#f9d94a;
  --yellow-deep:#f3c623;
  --text-grey:#808080;
  --canvas:#ffffff;
  --leaf-dark:#9a4a08;
  --leaf-mid:#e08a1c;
  --leaf-light:#f6c152;
}
*{box-sizing:border-box;margin:0;padding:0}
html,body{width:1200px;height:1000px;overflow:hidden;background:var(--canvas)}
body{position:relative;font-family:"Barlow",Arial,sans-serif}
.slide{position:absolute;width:349px;height:258px;background:#fff;overflow:hidden;
  box-shadow:2px 3px 5px rgba(0,0,0,.35)}
.s1{left:47px;top:150px}.s2{left:434px;top:150px}.s3{left:821px;top:150px}
.s4{left:47px;top:543px}.s5{left:434px;top:543px}.s6{left:821px;top:543px}
.shape{position:absolute;left:0;top:0;width:349px;height:258px}
.brand{position:absolute;color:var(--blue);font-weight:600;font-size:11px;letter-spacing:.3px}
.header-brand{right:11px;top:32px}
.cover-brand{right:11px;bottom:14px;font-size:13px}
.cover-title{position:absolute;left:15px;top:216px;color:var(--blue);font-size:15px;font-weight:500}
.cover-sub{position:absolute;left:15px;top:239px;color:var(--text-grey);font-size:9.5px}
.slide-title{position:absolute;left:10px;top:15px;color:#fff;font-size:15.5px;font-weight:500}
.footer{position:absolute;left:0;bottom:0;width:100%;height:6px;
  background:linear-gradient(90deg,var(--leaf-dark),var(--leaf-mid) 20%,var(--leaf-light) 40%,var(--leaf-mid) 60%,var(--leaf-dark) 80%,var(--leaf-mid))}
.footer-note{position:absolute;bottom:7px;left:145px;font-size:4.5px;color:var(--yellow-deep)}
.page-no{position:absolute;bottom:7px;right:10px;font-size:4.5px;color:var(--text-grey)}
.agenda{position:absolute;left:6px;top:73px;list-style:none}
.agenda li{display:flex;align-items:center;height:23px;font-size:9px;color:var(--blue);font-weight:500}
.agenda .time{width:50px;height:12px;margin-right:27px;background:var(--yellow);border-radius:1px;
  padding-left:3px;font-size:8px;font-weight:400;line-height:12px}
.agenda .who{color:var(--text-grey);font-weight:400;margin-left:3px}
.bullets{list-style:none;color:var(--text-grey)}
.bullets li{position:relative;padding-left:10px}
.bullets li::before{content:"";position:absolute;left:1px;top:.55em;width:3px;height:3px;border-radius:50%;background:var(--yellow-deep)}
.col{position:absolute;top:68px;width:155px}
.col-a{left:10px}.col-b{left:177px}
.col h3{color:var(--blue);font-size:9px;font-weight:600;margin-bottom:3px}
.col .bullets{font-size:7.5px;line-height:10.2px}
.col .bullets li{margin-bottom:3px}
.main-list{position:absolute;left:10px;top:62px;width:320px;font-size:10px;line-height:11px}
.main-list li{margin-bottom:5px}
.pic-list{position:absolute;left:10px;top:64px;width:172px;font-size:9.5px;line-height:11px}
.pic-list li{margin-bottom:5px}
.pic-frame{position:absolute;left:193px;top:64px;width:146px;height:118px;background:#fff;padding:3px;
  box-shadow:1px 1px 4px rgba(0,0,0,.35)}
.pic-fill{width:100%;height:100%;background:linear-gradient(135deg,#e9eef3,#c6d2de 45%,#7c8fa3 75%,#2a3440)}
</style>
</head>
<body>

<!-- Session title slide -->
<section class="slide s1">
  <div class="shape" role="img" aria-label="Close-up photograph of an orange autumn maple leaf on a blurred background"
       style="background:radial-gradient(ellipse at 55% 45%,#f3a32a,#c8660f 45%,#6f4a1c 80%,#3b3a22)"></div>
  <svg class="shape" viewBox="0 0 349 258">
    <path d="M0 204 C120 200 250 170 349 140 V258 H0Z" fill="#fff"/>
    <path d="M0 200 C120 196 250 166 349 134 V142 C250 174 120 204 0 208Z" fill="var(--yellow)"/>
    <rect x="0" y="254" width="349" height="4" fill="var(--blue)"/>
  </svg>
  <h1 class="cover-title">TRACING MANY PIPELINES</h1>
  <p class="cover-sub">October 14, 2010</p>
  <span class="brand cover-brand">Corvex</span>
</section>

<!-- Agenda slide -->
<section class="slide s2">
  <svg class="shape" viewBox="0 0 349 258">
    <path d="M0 0H349V22 C260 42 140 58 0 60Z" fill="var(--blue)"/>
    <path d="M0 60 C140 58 260 42 349 22 V30 C260 50 140 62 0 63Z" fill="var(--yellow)"/>
  </svg>
  <h2 class="slide-title">Agenda</h2>
  <span class="brand header-brand">Corvex</span>
  <ul class="agenda">
    <li><span class="time">7:30</span>Breakfast</li>
    <li><span class="time">8:00 – 8:20</span>Welcome, Keynote rant<span class="who">(Ron and Alan)</span></li>
    <li><span class="time">8:20 – 8:40</span>Financials<span class="who">(Mark and Paul)</span></li>
    <li><span class="time">8:40 – 9:05</span>Production Accounting<span class="who">(Dale)</span></li>
    <li><span class="time">9:05 – 9:20</span>Marketing<span class="who">(Rhys)</span></li>
    <li><span class="time">9:20 – 9:40</span>Other software and predictions<span class="who">(Neil and Grant)</span></li>
    <li><span class="time">9:40 – 10:00</span>Questions, discussion</li>
  </ul>
  <div class="footer"></div>
  <span class="footer-note">Advisory Partners</span><span class="page-no">2</span>
</section>

<!-- Functional area title slide -->
<section class="slide s3">
  <div class="shape" role="img" aria-label="Black and white close-up photograph of a maple leaf"
       style="background:radial-gradient(ellipse at 50% 45%,#9a9a9a,#5e5e5e 45%,#2e2e2e 80%,#1c1c1c)"></div>
  <svg class="shape" viewBox="0 0 349 258">
    <path d="M0 204 C120 200 250 170 349 140 V258 H0Z" fill="#fff"/>
    <path d="M0 200 C120 196 250 166 349 134 V142 C250 174 120 204 0 208Z" fill="var(--yellow)"/>
    <rect x="0" y="254" width="349" height="4" fill="var(--blue)"/>
  </svg>
  <h1 class="cover-title" style="font-size:13.5px">Financial Accounting</h1>
  <p class="cover-sub">Mark Ferris &amp; Paul Dunmore</p>
  <span class="brand cover-brand">Corvex</span>
</section>

<!-- Comparison slide -->
<section class="slide s4">
  <svg class="shape" viewBox="0 0 349 258">
    <path d="M0 0H349V16 C260 36 140 52 0 54Z" fill="var(--blue)"/>
    <path d="M0 54 C140 52 260 36 349 16 V24 C260 44 140 56 0 57Z" fill="var(--yellow)"/>
  </svg>
  <h2 class="slide-title">Comparison slide</h2>
  <span class="brand header-brand">Corvex</span>
  <div class="col col-a">
    <h3>Title A</h3>
    <ul class="bullets">
      <li>Lorem ipsum dolor sit amet, consectetur adipiscing elit.</li>
      <li>Mauris semper, enim ac congue hendrerit, orci ipsum cursus erat, in varius enim sem vel purus.</li>
      <li>Praesent lacus nibh, hendrerit nec porta ut, elementum et risus.</li>
      <li>Maecenas ultricies, mauris pretium dictum hendrerit, mi elit aliquam nisl, vitae ultricies nibh diam eu orci.</li>
    </ul>
  </div>
  <div class="col col-b">
    <h3>Title B</h3>
    <ul class="bullets">
      <li>Lorem ipsum dolor sit amet, consectetur adipiscing elit.</li>
      <li>Mauris semper, enim ac congue hendrerit, orci ipsum cursus erat, in varius enim sem vel purus.</li>
      <li>Praesent lacus nibh, hendrerit nec porta ut, elementum et risus.</li>
      <li>Maecenas ultricies, mauris pretium dictum hendrerit, mi elit aliquam nisl, vitae ultricies nibh diam eu orci.</li>
    </ul>
  </div>
  <div class="footer"></div>
  <span class="footer-note">Advisory Partners</span><span class="page-no">4</span>
</section>

<!-- Title with content slide -->
<section class="slide s5">
  <svg class="shape" viewBox="0 0 349 258">
    <path d="M0 0H349V16 C260 36 140 52 0 54Z" fill="var(--blue)"/>
    <path d="M0 54 C140 52 260 36 349 16 V24 C260 44 140 56 0 57Z" fill="var(--yellow)"/>
  </svg>
  <h2 class="slide-title">Norvane Ledger FM</h2>
  <span class="brand header-brand">Corvex</span>
  <ul class="bullets main-list">
    <li>Ledger FM user count is over 130</li>
    <li>Almost all new users are smaller and adopting the ASP model</li>
    <li>Core functionality and technology has not changed</li>
    <li>New features include technical currency, master file maintenance wizard and reversal engine for system-generated vouchers</li>
    <li>Norvane is focusing on the reporting layer across all their products, with Spectra being relevant to FM – product continues to evolve</li>
  </ul>
  <div class="footer"></div>
  <span class="footer-note">Advisory Partners</span><span class="page-no">5</span>
</section>

<!-- Picture with caption slide -->
<section class="slide s6">
  <svg class="shape" viewBox="0 0 349 258">
    <path d="M0 0H349V16 C260 36 140 52 0 54Z" fill="var(--blue)"/>
    <path d="M0 54 C140 52 260 36 349 16 V24 C260 44 140 56 0 57Z" fill="var(--yellow)"/>
  </svg>
  <h2 class="slide-title">Picture slide</h2>
  <span class="brand header-brand">Corvex</span>
  <ul class="bullets pic-list">
    <li>Lorem ipsum dolor sit amet, consectetur adipiscing elit.</li>
    <li>Mauris semper, enim ac congue hendrerit, orci ipsum cursus erat, in varius enim sem vel purus.</li>
    <li>Praesent lacus nibh, hendrerit nec porta ut, elementum et risus.</li>
    <li>Maecenas ultricies, mauris pretium dictum hendrerit, mi elit aliquam nisl, vitae ultricies nibh diam eu orci.</li>
  </ul>
  <div class="pic-frame">
    <div class="pic-fill" role="img" aria-label="Photograph of a hand using a calculator over printed financial charts"></div>
  </div>
  <div class="footer"></div>
  <span class="footer-note">Advisory Partners</span><span class="page-no">6</span>
</section>

</body>
</html>
```